Intelligent design image for our website

I would like an awesome image for our website that showcases the intelligent design of our app. We currently have a test web site here.
https://www.roadpliant.com.au/test-ewd/
I really do not like the graphic next to the "Intelligent design" and i want something much better than this.
Our app is used by Australian Truck Drivers. It would be nice to have a little bit of an Australian feel, but most importantly is should clearly showcase our app look a feel and the screens should be as legible (readable) as possible. These examples could be used for inspiration.
https://mockvendra.net/products/free-app-showcase-mockup-psd-5817402
https://www.plontrix.com/community/file/2294618830157362901/AppScreen-Intro-Page-Layout-for-Phone-Apps-Display

```html
<!DOCTYPE html>
<html lang="en">
<head>
<meta charset="utf-8">
<title>Intelligent design – app screens</title>
<link href="https://fonts.googleapis.com/css2?family=Lato:wght@400;700&display=swap" rel="stylesheet">
<style>
  :root{
    --bg:#ffffff;
    --card:#ffffff;
    --card-edge:#e3e8ee;
    --ink:#1d2127;
    --muted:#5d6570;
    --rule:#d9dee5;
    --blue:#2f9bd6;
    --blue-deep:#2c6fe8;
    --blue-soft:#9fc0f5;
    --blue-pale:#b9d7f7;
    --red:#e9857d;
    --red-pale:#f4b8b3;
    --grid:#d6d9de;
  }
  *{box-sizing:border-box;margin:0;padding:0}
  html,body{width:1200px;height:1200px;overflow:hidden;background:var(--bg)}
  body{font-family:"Lato",sans-serif;color:var(--ink);position:relative}

  .card{position:absolute;background:var(--card);border:1px solid var(--card-edge);border-radius:14px;box-shadow:0 14px 40px rgba(20,40,70,.12)}

  /* tab header */
  .tab{position:absolute;top:-1px;height:40px;background:var(--blue);color:#fff;font-size:19px;display:flex;align-items:center;justify-content:center;gap:10px;border-radius:0 0 10px 10px}
  .info{position:absolute;right:24px;top:14px;width:28px;height:28px}

  .stat{text-align:center}
  .stat .value{font-weight:700;font-size:22px}
  .stat .label{font-size:15px;color:var(--muted);margin-top:2px;line-height:1.15}
  .btn{display:inline-block;border:1.5px solid var(--blue);color:var(--blue);border-radius:6px;font-size:15px;padding:8px 18px;background:#fff}

  /* 14 day rule */
  .rule-card{left:300px;top:90px;width:600px;padding-bottom:20px}
  .rule-card .tab{left:220px;width:200px}
  .period-row{display:flex;justify-content:space-around;padding:56px 40px 18px;border-bottom:2px solid var(--blue)}

  .progress{padding:22px 24px 10px}
  .progress .label{font-size:15px;color:var(--muted)}
  .bar{margin-top:14px;height:16px;border-radius:8px;background:var(--blue-soft);overflow:hidden}
  .bar span{display:block;width:54%;height:100%;background:var(--blue-deep);border-radius:8px 0 0 8px}
  .scale{display:flex;justify-content:space-between;font-size:13px;color:var(--muted);margin-top:6px}

  .grid{display:grid;grid-template-columns:1fr 1fr;margin:6px 24px 0}
  .grid .stat{padding:16px 0;border-top:1px solid var(--rule)}
  .grid .stat:nth-child(odd){border-right:1px solid var(--rule)}

  .pager{display:flex;align-items:center;justify-content:space-between;padding:12px 60px 0}
  .pager .stat .value{font-size:18px}

  /* night rests */
  .night-card{left:200px;top:710px;width:560px;padding-bottom:26px}
  .night-card .tab{left:250px;width:220px;background:var(--blue-pale)}
  .bed{width:34px;height:20px}
  .night-top{padding:58px 0 16px 60px;border-bottom:2px solid var(--blue-pale)}
  .night-next{padding:18px 0 18px 50px;border-bottom:1px solid var(--rule)}
  .days{display:grid;grid-template-columns:repeat(5,46px);gap:20px 44px;padding:22px 0 0 48px}
  .day{width:44px;height:44px;border-radius:50%;border:2px solid var(--blue-pale);color:var(--blue);font-size:15px;display:flex;align-items:center;justify-content:center;position:relative}
  .day.missed{border-color:var(--red-pale);color:var(--red)}
  .day.missed::after{content:"";position:absolute;left:4px;right:4px;top:50%;height:2px;background:var(--red);transform:rotate(40deg)}
  .night-card .btn{margin:24px 0 0 50px;border-color:var(--blue-pale);color:var(--blue-pale)}

  /* chart */
  .chart-card{left:730px;top:690px;width:300px;height:340px}
  .chart-card svg{position:absolute;inset:0}
  .axis text{font-family:"Lato",sans-serif;font-size:15px;fill:var(--muted)}
</style>
</head>
<body>

<section class="card rule-card" aria-label="14 day rule">
  <div class="tab">14 day Rule</div>
  <svg class="info" viewBox="0 0 28 28" aria-hidden="true"><circle cx="14" cy="14" r="12" fill="none" stroke="#2f9bd6" stroke-width="2"/><rect x="12.8" y="12" width="2.4" height="9" fill="#2f9bd6"/><circle cx="14" cy="8.5" r="1.6" fill="#2f9bd6"/></svg>

  <div class="period-row">
    <div class="stat"><div class="value">01:17 14-Aug</div><div class="label">Period Start</div></div>
    <div class="stat"><div class="value">01:17 28-Aug</div><div class="label">Period End</div></div>
  </div>

  <div class="progress">
    <div class="label">Work Completed</div>
    <div class="bar"><span></span></div>
    <div class="scale"><span>0 hr</span><span>144 hr</span></div>
  </div>

  <div class="grid">
    <div class="stat"><div class="value">78:08</div><div class="label">Work Completed</div></div>
    <div class="stat"><div class="value">43:01</div><div class="label">Maximum Continuous Rest</div></div>
    <div class="stat"><div class="value">65:52</div><div class="label">Work Remaining</div></div>
    <div class="stat"><div class="value">01:17 27-Aug</div><div class="label">Start 24 hr Rest Before</div></div>
    <div class="stat"><div class="value">62:29</div><div class="label">Period<br>Remaining</div></div>
    <div class="stat"><div class="value">1 / 2</div><div class="label">24 hr Rests<br>Found/Required</div></div>
  </div>

  <div class="pager">
    <span class="btn">&lt; Previous</span>
    <div class="stat"><div class="value">1/4</div><div class="label">Active Periods</div></div>
    <span class="btn">Next &gt;</span>
  </div>
</section>

<section class="card night-card" aria-label="Night rests">
  <div class="tab">
    <svg class="bed" viewBox="0 0 34 20" aria-hidden="true"><path d="M2 3v15M2 13h30v5M6 9h8v4H6zM16 8h14a2 2 0 0 1 2 2v3H16z" fill="none" stroke="#e9857d" stroke-width="2"/></svg>
    Night Rests
  </div>
  <div class="night-top stat" style="text-align:left">
    <div class="value">17 Aug</div><div class="label">Period Start</div>
  </div>
  <div class="night-next stat" style="text-align:left">
    <div class="value">01:00 29-Aug</div><div class="label">Start Next<br>Night Rest Before</div>
  </div>
  <div class="days">
    <span class="day">12</span><span class="day">13</span><span class="day missed">14</span><span class="day missed">15</span><span class="day">16</span>
    <span class="day missed">19</span><span class="day missed">20</span><span class="day missed">21</span><span class="day">22</span><span class="day missed">23</span>
  </div>
  <span class="btn">&lt; Previous</span>
</section>

<section class="card chart-card" aria-label="Daily hours chart">
  <svg viewBox="0 0 300 340">
    <g stroke="#d6d9de" stroke-width="1.5">
      <line x1="20" y1="42" x2="252" y2="42"/><line x1="20" y1="90" x2="252" y2="90"/>
      <line x1="20" y1="138" x2="252" y2="138"/><line x1="20" y1="186" x2="252" y2="186"/>
      <line x1="20" y1="234" x2="252" y2="234"/><line x1="20" y1="282" x2="252" y2="282"/>
    </g>
    <g class="axis" text-anchor="middle">
      <text x="276" y="22">24</text><text x="276" y="70">20</text><text x="276" y="118">16</text>
      <text x="276" y="166">12</text><text x="276" y="214">8</text><text x="276" y="262">4</text>
    </g>
    <g stroke-linecap="round" stroke-width="16">
      <line x1="75" y1="230" x2="75" y2="318" stroke="#9fc0f5"/>
      <line x1="145" y1="210" x2="145" y2="310" stroke="#9fc0f5"/>
      <line x1="215" y1="230" x2="215" y2="300" stroke="#2c6fe8"/>
    </g>
  </svg>
</section>

</body>
</html>
```